Sports Betting Business Consultant

After 21 years in corporate life. Will be continue as consultant/advisor in sports betting industry. Need a business card. Prefer an iphone format as layout. Elements; betting,ticket, sports types soccer, basketball, tennis etc , odds etc.

```html
<!DOCTYPE html>
<html lang="en">
<head>
<meta charset="utf-8">
<title>Deniz Arslan – Sports Betting Business Consultant</title>
<link rel="stylesheet" href="https://fonts.googleapis.com/css2?family=Arimo:wght@400&family=Rokkitt:wght@400;700&display=swap">
<style>
  :root {
    --page: #ffffff;
    --frame: #000000;
    --back-panel: #1b1b1b;
    --grad-pink: #d36aad;
    --grad-violet: #a487c9;
    --grad-blue: #7b9ee0;
    --panel-pink: #f1d3e8;
    --panel-blue: #dbe2f5;
    --green-deep: #4e9e4f;
    --green-soft: #7fc49f;
    --envelope-red: #931303;
    --ink: #1a1a1a;
    --ink-soft: #4f4a52;
    --clock: #f3eeee;
    --white: #ffffff;
  }
  html, body {
    margin: 0;
    padding: 0;
    width: 1200px;
    height: 1200px;
    overflow: hidden;
    background: var(--page);
  }
  .canvas {
    position: relative;
    width: 1200px;
    height: 1200px;
  }
  .device-art {
    position: absolute;
    inset: 0;
  }
  .card-text {
    position: absolute;
    left: 157px;
    width: 396px;
    margin: 0;
    text-align: center;
  }
  .clock {
    top: 368px;
    font-family: "Arimo", Arial, sans-serif;
    font-size: 104px;
    line-height: 1;
    color: var(--clock);
    letter-spacing: -1px;
  }
  .name {
    top: 495px;
    left: 137px;
    width: 436px;
    font-family: "Rokkitt", "Rockwell", serif;
    font-weight: 700;
    font-size: 58px;
    line-height: 1;
    color: var(--ink);
  }
  .role {
    top: 567px;
    font-family: "Rokkitt", "Rockwell", serif;
    font-weight: 400;
    font-size: 27px;
    line-height: 31px;
    color: var(--ink-soft);
    letter-spacing: 0.3px;
  }
  .email {
    top: 803px;
    font-family: "Rokkitt", "Rockwell", serif;
    font-size: 30px;
    line-height: 1;
    color: var(--ink);
  }
  .phone-number {
    top: 918px;
    left: 270px;
    width: auto;
    text-align: left;
    font-family: "Arimo", Arial, sans-serif;
    font-size: 29px;
    line-height: 1;
    color: var(--white);
  }
</style>
</head>
<body>
<main class="canvas">
  <svg class="device-art" width="1200" height="1200" viewBox="0 0 1200 1200" aria-hidden="true">
    <defs>
      <linearGradient id="screen-gradient" x1="0" x2="1" y1="0" y2="0">
        <stop offset="0" stop-color="var(--grad-pink)"/>
        <stop offset="0.5" stop-color="var(--grad-violet)"/>
        <stop offset="1" stop-color="var(--grad-blue)"/>
      </linearGradient>
      <linearGradient id="panel-gradient" x1="0" x2="1" y1="0" y2="0">
        <stop offset="0" stop-color="var(--panel-pink)"/>
        <stop offset="1" stop-color="var(--panel-blue)"/>
      </linearGradient>
      <linearGradient id="call-gradient" x1="0" x2="1" y1="0" y2="0">
        <stop offset="0" stop-color="var(--green-deep)"/>
        <stop offset="1" stop-color="var(--green-soft)"/>
      </linearGradient>
      <clipPath id="screen-clip">
        <rect x="157" y="248" width="396" height="746" rx="40"/>
      </clipPath>
    </defs>

    <!-- front of card -->
    <g class="card-front">
      <rect class="front-frame" x="131" y="226" width="449" height="790" rx="72" fill="var(--frame)"/>
      <g clip-path="url(#screen-clip)">
        <rect class="screen" x="157" y="248" width="396" height="746" fill="url(#screen-gradient)"/>
        <rect class="contact-panel" x="157" y="697" width="396" height="179" rx="14" fill="url(#panel-gradient)"/>
        <rect class="call-band" x="157" y="881" width="396" height="113" rx="14" fill="url(#call-gradient)"/>
      </g>
      <path class="notch" d="M244 248 H469 V258 Q469 274 453 274 H260 Q244 274 244 258 Z" fill="var(--frame)"/>
      <rect class="speaker" x="324" y="254" width="61" height="6" rx="3" fill="#3a3a3a"/>
      <circle class="front-camera" cx="403" cy="256" r="6" fill="#3a3a3a"/>

      <g class="status-signal" fill="var(--white)">
        <rect x="177" y="272" width="4" height="6"/>
        <rect x="184" y="268" width="4" height="10"/>
        <rect x="191" y="264" width="4" height="14"/>
        <rect x="198" y="259" width="4" height="19"/>
      </g>
      <g class="status-wifi" fill="none" stroke="var(--white)" stroke-width="3" stroke-linecap="round">
        <path d="M214 267 Q228 256 242 267"/>
        <path d="M219 272 Q228 265 237 272"/>
        <circle cx="228" cy="277" r="2" fill="var(--white)" stroke="none"/>
      </g>
      <g class="status-battery">
        <rect x="487" y="263" width="31" height="14" rx="2" fill="none" stroke="var(--white)" stroke-width="2"/>
        <rect x="519" y="267" width="3" height="6" fill="var(--white)"/>
        <g fill="var(--white)">
          <rect x="490" y="266" width="5" height="8"/>
          <rect x="497" y="266" width="5" height="8"/>
          <rect x="504" y="266" width="5" height="8"/>
          <rect x="511" y="266" width="5" height="8"/>
        </g>
      </g>

      <g class="email-icon">
        <circle cx="354" cy="754" r="32" fill="var(--envelope-red)"/>
        <rect x="335" y="742" width="38" height="25" fill="var(--white)"/>
        <path d="M335 742 L354 757 L373 742 M335 767 L349 754 M373 767 L359 754" fill="none" stroke="var(--envelope-red)" stroke-width="1.8"/>
      </g>

      <path class="call-icon" d="M221 913 C215 919 217 932 228 945 C240 959 254 966 261 961 L266 956 C268 954 267 951 265 950 L254 943 C252 942 250 942 248 944 L244 948 C238 945 230 937 227 931 L231 927 C233 925 233 923 232 921 L226 911 C225 909 222 909 221 910 Z" fill="var(--white)"/>
    </g>

    <!-- back of card -->
    <g class="card-back">
      <rect class="back-frame" x="639" y="226" width="447" height="788" rx="72" fill="var(--frame)"/>
      <rect class="back-panel" x="652" y="272" width="424" height="707" rx="30" fill="var(--back-panel)"/>
      <g class="camera-module">
        <rect x="689" y="300" width="61" height="126" rx="30" fill="#8c8c8c"/>
        <rect x="692" y="303" width="55" height="120" rx="27" fill="#0a0a14"/>
        <circle cx="720" cy="330" r="12" fill="#10163a"/>
        <circle cx="720" cy="330" r="4" fill="#2a4aa8"/>
        <circle cx="720" cy="363" r="10" fill="#e3c784"/>
        <circle cx="720" cy="363" r="5" fill="#fff6d8"/>
        <circle cx="720" cy="393" r="12" fill="#10163a"/>
        <circle cx="720" cy="393" r="4" fill="#2a4aa8"/>
      </g>
    </g>
  </svg>

  <p class="card-text clock">0:00</p>
  <h1 class="card-text name">Deniz Arslan</h1>
  <p class="card-text role">Sports Betting Business<br>Consultant</p>
  <p class="card-text email">dnzarsln@postmail.com</p>
  <p class="card-text phone-number">+90 555 0142087</p>
</main>
</body>
</html>
```